Van sign writing, looking for something simple and corporate

Am after some design ideas for the sign writing of my 2016 Morvane kelvor van. Design ideas can be taken from my website if need be. www.brantlypower.com.au
Or my Chatterly page
(Just search brantly power on Chatterly)

Only looking at sign writing both sides

Im really looking for something thats pretty simple, yet effective.

Was thinking of having a washed out, light grey logo down the side of the whole van, on a 20 degree angle, with some points written around it.

Your design doesn't have to be that, I'm very open to ideas

have included logo and flyer we use in attachments

Industry/Entity Type

Electrician

Requirements
Must have
• Phone number
• Email
• Website
• Paytek available
• Licence number
• Abn

```html
<!DOCTYPE html>
<html lang="en">
<head>
<meta charset="utf-8">
<title>Brantly Power – Van Side Livery</title>
<link href="https://fonts.googleapis.com/css2?family=Roboto:wght@300;400;700&display=swap" rel="stylesheet">
<style>
  :root {
    --backdrop: #1e1f21;
    --body-white: #ffffff;
    --panel-line: #d9d9d9;
    --band-grey: #8a8b8d;
    --band-edge: #3b3c3e;
    --ink: #333333;
    --ink-soft: #555555;
    --accent-blue: #2ea3e0;
    --pay-red: #a32f4f;
    --on-band: #ffffff;
  }
  html, body {
    margin: 0;
    width: 1200px;
    height: 960px;
    overflow: hidden;
    background: var(--backdrop);
  }
  .livery {
    display: block;
    width: 1200px;
    height: 960px;
    font-family: "Roboto", Arial, sans-serif;
  }
  .van-body { fill: var(--body-white); }
  .panel-seam { stroke: var(--panel-line); stroke-width: 1.5; fill: none; }
  .grey-band { fill: var(--band-grey); }
  .band-edge { stroke: var(--band-edge); stroke-width: 7; }
  .contact-line { font-size: 16px; fill: var(--ink-soft); }
  .contact-line .strong { font-weight: 700; fill: var(--ink); }
  .pay-badge { fill: var(--pay-red); }
  .pay-name { font-size: 12px; font-weight: 700; fill: #ffffff; }
  .pay-available { font-size: 18px; font-weight: 700; fill: var(--ink); }
  .brand-name { font-size: 42px; font-weight: 300; fill: var(--ink); letter-spacing: 1px; }
  .phone-number { font-size: 38px; font-weight: 700; fill: var(--ink); }
  .phone-icon { fill: var(--accent-blue); }
  .email-icon { fill: var(--accent-blue); }
  .social-square { fill: var(--accent-blue); }
  .reg-detail { font-size: 12px; fill: var(--on-band); }
  .reg-detail .label { font-weight: 700; }
  .web-address { font-size: 20px; fill: var(--on-band); }
  .web-address .strong { font-weight: 700; }
</style>
</head>
<body>
<svg class="livery" viewBox="0 0 1200 960" xmlns="http://www.w3.org/2000/svg">
  <defs>
    <clipPath id="body-shape">
      <path d="M30,350 Q30,325 70,325 L900,330 Q960,335 1010,370 L1100,470 Q1140,500 1140,560 L1140,740 L1006,740 A90,90 0 0 0 826,740 L374,740 A90,90 0 0 0 194,740 L30,740 Z"/>
    </clipPath>
  </defs>

  <!-- van side panel -->
  <g class="van-side">
    <path class="van-body" d="M30,350 Q30,325 70,325 L900,330 Q960,335 1010,370 L1100,470 Q1140,500 1140,560 L1140,740 L1006,740 A90,90 0 0 0 826,740 L374,740 A90,90 0 0 0 194,740 L30,740 Z"/>
    <g clip-path="url(#body-shape)">
      <polygon class="grey-band" points="20,558 830,724 830,760 20,760"/>
      <line class="band-edge" x1="20" y1="558" x2="830" y2="724"/>
      <line class="panel-seam" x1="428" y1="348" x2="428" y2="740"/>
      <line class="panel-seam" x1="766" y1="350" x2="766" y2="740"/>
      <line class="panel-seam" x1="118" y1="536" x2="428" y2="536"/>
    </g>
  </g>

  <!-- contact block -->
  <g class="contact-block">
    <rect class="email-icon" x="110" y="374" width="18" height="13" rx="1"/>
    <path d="M110,375 L119,382 L128,375" stroke="#ffffff" stroke-width="1.5" fill="none"/>
    <text class="contact-line" x="133" y="387"><tspan class="strong">brantlypower</tspan>@mailhaven.com</text>

    <rect class="social-square" x="101" y="412" width="18" height="18" rx="2"/>
    <text class="contact-line" x="127" y="427">chatterly.com/<tspan class="strong">brantlypower</tspan>/</text>

    <rect class="pay-badge" x="98" y="451" width="54" height="35" rx="2"/>
    <text class="pay-name" x="125" y="473" text-anchor="middle">Paytek</text>
    <text class="pay-available" x="165" y="476">available</text>
  </g>

  <!-- brand name -->
  <text class="brand-name" x="584" y="590" text-anchor="middle">brantly power</text>

  <!-- phone -->
  <g class="phone-block">
    <path class="phone-icon" d="M748,563 l8,-2 l5,10 l-5,4 q3,9 11,14 l4,-5 l10,5 l-2,8 q-4,3 -10,1 q-20,-8 -24,-26 q-1,-6 3,-9 z"/>
    <text class="phone-number" x="782" y="595">0400 318 726</text>
  </g>

  <!-- registration details -->
  <text class="reg-detail" x="50" y="638"><tspan class="label">NSW Lic No:</tspan> 104512C</text>
  <text class="reg-detail" x="50" y="662"><tspan class="label">ABN No:</tspan> 51 824 753 556</text>

  <!-- website -->
  <text class="web-address" x="434" y="728">www.<tspan class="strong">brantlypower</tspan>.com.au</text>
</svg>
</body>
</html>
```